Mr Pellows Lawn Care flyer for newsletter

I need a professional looking flyer design for my company Mr Pellows Lawn Care based in New Braunfels, TX to boost sales. Must include the following: Lawn service starting at $40 (mowing, edging, leaf blowing) Tree trimming starting at $125. Other services-mulching, shrub trimming, aeration, flower bed maintenance, Fall/spring clean up. Serving New Braunfels and surrounding areas. To set up and estimate please call 830 247 3091 or email mrpellowslawn@brimfield-mail.com

Industry/Entity Type

Landscaping

Font styles to use
Serif

Colors

Designer to choose colors to be used in the design.

Requirements
Must have
• Phone number 830 247 3091
• Email mrpellowslawn@brimfield-mail.com

```html
<!DOCTYPE html>
<html lang="en">
<head>
<meta charset="utf-8">
<title>Mr Pellows Lawn Care – Flyer</title>
<link rel="stylesheet" href="https://fonts.googleapis.com/css2?family=Lato:wght@400;700;900&family=Source+Sans+3:wght@600;700&display=swap">
<style>
  :root {
    --backdrop: #3b3b3d;
    --lime: #d4e48c;
    --forest: #0b6a2e;
    --forest-deep: #075624;
    --cream-ring: #eef5cf;
    --price-red: #e0272a;
    --ink: #1a1a1a;
    --mist: #e7e8e9;
    --white: #ffffff;
  }
  * { margin: 0; padding: 0; box-sizing: border-box; }
  html, body { width: 839px; height: 1200px; overflow: hidden; }
  body { background: var(--backdrop); position: relative; font-family: "Lato", sans-serif; }

  .flyer {
    position: absolute; left: 58px; top: 88px;
    width: 862px; height: 1220px;
    transform: scale(0.8376); transform-origin: top left;
    background: var(--lime); overflow: hidden;
  }
  .flyer > * { position: absolute; }
  .backdrop-art { left: 0; top: 0; width: 862px; height: 1220px; }

  .service-area {
    right: 22px; top: 34px; text-align: right;
    font-family: "Source Sans 3", sans-serif; font-weight: 700;
    font-size: 33px; line-height: 41px; color: var(--white);
  }

  .brand-name {
    left: 492px; top: 300px; width: 356px; text-align: center;
    font-family: "Lato", sans-serif; font-weight: 900;
    font-size: 64px; line-height: 84px; color: var(--forest);
    white-space: nowrap;
  }

  .offer { left: 22px; color: var(--ink); }
  .offer-title {
    font-family: "Source Sans 3", sans-serif; font-weight: 700;
    color: var(--forest); font-size: 45px; line-height: 44px;
  }
  .offer-from { font-size: 52px; line-height: 54px; }
  .offer-note { font-size: 31px; line-height: 38px; }
  .lawn-offer { top: 565px; }
  .tree-offer { top: 740px; }

  .price {
    color: var(--price-red); font-family: "Source Sans 3", sans-serif;
    font-weight: 700; line-height: 1;
  }
  .price-lawn { left: 296px; top: 560px; font-size: 108px; }
  .price-lawn .currency { font-size: 62px; vertical-align: 22px; }
  .price-tree { left: 292px; top: 740px; font-size: 108px; }
  .price-tree .currency { font-size: 36px; vertical-align: 0; margin-right: 4px; }

  .extra-services {
    left: 518px; top: 585px; list-style: none;
    font-family: "Source Sans 3", sans-serif; font-weight: 700;
    font-size: 27px; color: var(--forest);
  }
  .extra-services li { height: 48px; line-height: 40px; padding-left: 28px; position: relative; }
  .extra-services li::before {
    content: ""; position: absolute; left: 0; top: 14px;
    width: 11px; height: 11px; background: var(--price-red);
  }

  .contact {
    left: 0; top: 890px; width: 862px; text-align: center;
    font-size: 31px; line-height: 40px; color: var(--ink);
  }
  .contact strong { font-weight: 700; }
  .contact .lead { font-weight: 700; font-family: "Source Sans 3", sans-serif; font-size: 33px; }
</style>
</head>
<body>
<div class="flyer">
  <svg class="backdrop-art" viewBox="0 0 862 1220" xmlns="http://www.w3.org/2000/svg">
    <defs>
      <radialGradient id="turf" cx="45%" cy="55%" r="65%">
        <stop offset="0" stop-color="#4fa63a"/>
        <stop offset="0.6" stop-color="#2f7d22"/>
        <stop offset="1" stop-color="#1d4d16"/>
      </radialGradient>
      <linearGradient id="grass-strip" x1="0" y1="0" x2="0" y2="1">
        <stop offset="0" stop-color="#e7e8e9"/>
        <stop offset="0.35" stop-color="#8fc46a"/>
        <stop offset="1" stop-color="#2f7f24"/>
      </linearGradient>
      <linearGradient id="thumb" x1="0" y1="0" x2="1" y2="1">
        <stop offset="0" stop-color="#7cb35a"/>
        <stop offset="1" stop-color="#2f6d22"/>
      </linearGradient>
    </defs>

    <rect class="header-band" x="380" y="0" width="482" height="146" fill="var(--forest)"/>
    <rect x="470" y="152" width="392" height="13" fill="var(--forest)"/>
    <rect x="470" y="177" width="392" height="15" fill="var(--forest)"/>
    <rect x="470" y="202" width="392" height="14" fill="var(--forest)"/>
    <rect x="470" y="226" width="392" height="13" fill="var(--forest)"/>

    <circle cx="222" cy="250" r="268" fill="var(--cream-ring)"/>
    <g role="img" aria-label="Photo of a ride-on lawn mower cutting a bright green lawn">
      <circle cx="222" cy="250" r="260" fill="url(#turf)"/>
    </g>

    <rect x="0" y="862" width="862" height="8" fill="var(--forest)"/>
    <rect x="0" y="870" width="862" height="150" fill="var(--mist)"/>
    <g role="img" aria-label="Photo strip of tall green grass">
      <rect x="0" y="1020" width="862" height="200" fill="url(#grass-strip)"/>
    </g>

    <g class="service-thumbs" fill="url(#thumb)" stroke="var(--white)" stroke-width="4">
      <circle cx="96" cy="1125" r="70" role="img" aria-label="Photo of a push mower on grass"/>
      <circle cx="263" cy="1125" r="70" role="img" aria-label="Photo of a worker using a leaf blower"/>
      <circle cx="431" cy="1125" r="70" role="img" aria-label="Photo of a tree being trimmed"/>
      <circle cx="598" cy="1125" r="70" role="img" aria-label="Photo of a neatly edged lawn"/>
      <circle cx="767" cy="1125" r="70" role="img" aria-label="Photo of hedge trimmer shaping a shrub"/>
    </g>
  </svg>

  <p class="service-area">Serving New Braunfels &amp;<br>Surrounding Areas.</p>

  <h1 class="brand-name">Mr Pellows<br>Lawn Care</h1>

  <div class="offer lawn-offer">
    <p class="offer-title">Lawn Service</p>
    <p class="offer-from">starting at</p>
    <p class="offer-note">(mowing, edging, leaf blowing)</p>
  </div>
  <p class="price price-lawn"><span class="currency">$</span>40</p>

  <div class="offer tree-offer">
    <p class="offer-title">Tree Trimming</p>
    <p class="offer-from">starting at</p>
  </div>
  <p class="price price-tree"><span class="currency">$</span>125</p>

  <ul class="extra-services">
    <li>Mulching</li>
    <li>Shrub Trimming</li>
    <li>Aeration</li>
    <li>Flower Bed Maintenance</li>
    <li>Fall/Spring Clean Up</li>
  </ul>

  <div class="contact">
    <p class="lead">To set up and estimates</p>
    <p><strong>Call:</strong> 830 247 3091</p>
    <p><strong>Email:</strong> mrpellowslawn@brimfield-mail.com</p>
  </div>
</div>
</body>
</html>
```